Norvane Builders Business Card

Modern and Professional Business Card for a Med size construction/development company.

See the samples below for the design I like … but I need ideas for incorporating the red company logo while still keeping the clean look of the card samples that are attached.

Logo and tag line on the back … info on the front.

Tagline: Quality Starts from the Ground Up

Target Market(s)

Med-Large General Contractors

Contact Information for Business Card

Norvane Builders Limited
42 Brenton Street
Elk Harbour, NL
B3K 7T2

t: 709-555-0147
f: 709-555-0192
w: www.norvanebuilders-example.com

Font styles to use
Sans Serif

Colors
fbee3e

Requirements
Must have
• I like the black and yellow designs of the attached samples …. but I'm not sure how to incorporate the red Norvane Builders logo into that design??
Nice to have
• Construction safety strips

```html
<!DOCTYPE html>
<html lang="en">
<head>
<meta charset="utf-8">
<title>Norvane Builders Business Card</title>
<link rel="stylesheet" href="https://fonts.googleapis.com/css2?family=Archivo:wght@700;800&display=swap">
<style>
  :root {
    --backdrop: #2f2f2f;
    --safety-yellow: #f5d90f;
    --ink-black: #0a0a0a;
    --signal-red: #e3202a;
    --paper-white: #ffffff;
  }
  * { box-sizing: border-box; margin: 0; padding: 0; }
  html, body {
    width: 1200px; height: 675px; overflow: hidden;
    background: var(--backdrop);
    font-family: "Archivo", Arial, sans-serif;
    font-weight: 800;
  }
  .stage { position: relative; width: 1200px; height: 675px; }
  .card {
    position: absolute; width: 500px; height: 286px; overflow: hidden;
    box-shadow: 0 14px 30px rgba(0,0,0,.45);
  }
  .safety-strip {
    position: absolute; left: 0; width: 100%; height: 16px;
  }
  /* Front */
  .card-front { left: 650px; top: 70px; background: var(--safety-yellow); color: var(--ink-black); }
  .card-front .safety-strip {
    background: repeating-linear-gradient(-45deg, var(--ink-black) 0 12px, var(--safety-yellow) 12px 34px);
  }
  .card-front .strip-top { top: 6px; }
  .card-front .strip-bottom { bottom: 6px; }
  .company-name {
    position: absolute; top: 32px; right: 24px;
    color: var(--signal-red); font-size: 25px; letter-spacing: .5px;
  }
  .emblem-area {
    position: absolute; left: 22px; top: 74px; width: 108px; height: 108px;
    border-radius: 50%; background: var(--ink-black); opacity: .85;
  }
  .person {
    position: absolute; right: 26px; top: 112px; text-align: right;
    font-size: 18px; line-height: 1.2;
  }
  .contact-list {
    position: absolute; left: 144px; top: 118px; list-style: none;
    font-size: 14px; line-height: 1.1;
  }
  .contact-item { display: flex; align-items: center; gap: 8px; margin-bottom: 7px; }
  .contact-icon { width: 20px; height: 20px; flex: none; }
  /* Back */
  .card-back { left: 60px; top: 330px; background: var(--ink-black); color: var(--paper-white); }
  .card-back .safety-strip {
    height: 20px;
    background: repeating-linear-gradient(-45deg, var(--safety-yellow) 0 18px, var(--ink-black) 18px 34px);
  }
  .card-back .strip-top { top: 10px; }
  .card-back .strip-bottom { bottom: 10px; }
  .brand-name {
    position: absolute; left: 0; right: 0; top: 104px; text-align: center;
    font-size: 30px; color: var(--paper-white); letter-spacing: .5px;
  }
  .tagline {
    position: absolute; left: 0; right: 0; top: 200px; text-align: center;
    font-size: 17px; letter-spacing: 1px;
  }
</style>
</head>
<body>
<main class="stage">
  <section class="card card-back" aria-label="Card back">
    <div class="safety-strip strip-top"></div>
    <p class="brand-name">NORVANE BUILDERS LIMITED</p>
    <p class="tagline">QUALITY STARTS FROM THE GROUND UP</p>
    <div class="safety-strip strip-bottom"></div>
  </section>

  <section class="card card-front" aria-label="Card front">
    <div class="safety-strip strip-top"></div>
    <p class="company-name">NORVANE BUILDERS LIMITED</p>
    <div class="emblem-area" role="img" aria-label="Gear and wrench emblem"></div>
    <p class="person">NAME<br>JOB TITLE</p>
    <ul class="contact-list">
      <li class="contact-item">
        <svg class="contact-icon" viewBox="0 0 20 20"><circle cx="10" cy="10" r="10" fill="#e3202a"/><path d="M6.5 5.5l2 2-1 1.2a7 7 0 0 0 3.8 3.8l1.2-1 2 2-1.2 1.4C9.5 14.5 5.5 10.5 5.1 6.7z" fill="#fff"/></svg>
        <span>709-555-0147</span>
      </li>
      <li class="contact-item">
        <svg class="contact-icon" viewBox="0 0 20 20"><circle cx="10" cy="10" r="10" fill="#e3202a"/><rect x="7" y="4.5" width="6" height="3.5" fill="#fff"/><rect x="5" y="8" width="10" height="5" rx="1" fill="#fff"/><rect x="7" y="12" width="6" height="3.5" fill="#fff" stroke="#e3202a" stroke-width=".8"/></svg>
        <span>709-555-0192</span>
      </li>
      <li class="contact-item">
        <svg class="contact-icon" viewBox="0 0 20 20"><circle cx="10" cy="10" r="10" fill="#e3202a"/><path d="M10 4a4 4 0 0 1 4 4c0 3-4 7.5-4 7.5S6 11 6 8a4 4 0 0 1 4-4z" fill="#fff"/><circle cx="10" cy="8" r="1.5" fill="#e3202a"/></svg>
        <span>42 BRENTON STREET<br>ELK HARBOUR, NL, B3K 7T2</span>
      </li>
      <li class="contact-item">
        <svg class="contact-icon" viewBox="0 0 20 20"><circle cx="10" cy="10" r="10" fill="#e3202a"/><g fill="none" stroke="#fff" stroke-width="1.1"><circle cx="10" cy="10" r="5.5"/><ellipse cx="10" cy="10" rx="2.4" ry="5.5"/><path d="M4.5 10h11M5.5 7h9M5.5 13h9"/></g></svg>
        <span>WWW.NORVANEBUILDERS-EXAMPLE.COM</span>
      </li>
    </ul>
    <div class="safety-strip strip-bottom"></div>
  </section>
</main>
</body>
</html>
```